Business Card for an IT Financial Company

Hi everybody,

We're a Brazilian company with the target of build a business card at the same time "formal and cool". We're looking for a revolutionary style, but no so informal or agressive. We like the UV effect and we can use 1 or more colors and sides. The brand is "vek" and you can see the logo attacked. The slogan is "Robôs Investidores" (investor robots).

Our site is [url removed, login to view] where you can see the vek screens. Observe that the Solaria is the main logo at the moment. We're changing for vek.

The texts on the card are: Tiago Lauro Bettencourt (name), CEO, 11 3516-9240 (company phone), 11 96048 2195 (mobile phone), tiago@[url removed, login to view] and www.solaria.com.br.

---- About the company ----

Our company is dedicated to building the most state of the art investment Robots. Our Robots identify the best opportunities to profit, capitalize on growth and effectively trade. We connect the vek interface with varies strategies that meet investors expectations from conservative to aggressive.

We have designed a secure yet flexible solution. Our goal is to assist our customer in achieving consistent profits in the financial market. We develop technologies that optimize the forms of investing in the financial markets with fast, secure and profitable Robots.

Without the influence of emotion or operational errors, the Robot analyses stocks in the financial markets. Utilizing indicators they operate automaticly, all of this happens within fractions of a second.

Get to know vek, a sympathetic web system that allows you to operate with strategies developed by market specialists. Choose a compatible profile that fits your lifestyle and link it directly to your investment account.

Diversify your portfolio with different Robots and profiles utilizing exclusive sophisticated mathematical strategies that minimize your exposure to risks. Increase your profits with total control.

We're specialists in Robots and pioneer in the use of Robots as a Service (RaaS) and has professional teams composed of financial and IT experts. The Robots operate at top speeds and offer operational security, continuous support and focus on research and development.

We take pride in our innovating systems, which is powerful yet has user friendly interfaces. Our online solution has a simple design, is flexible and instinctive. It also assists the user with investment diversification and minimizes trading risks.

```html
<!DOCTYPE html>
<html lang="pt-BR">
<head>
<meta charset="utf-8">
<title>vek — Cartão de visita</title>
<link href="https://fonts.googleapis.com/css2?family=Open+Sans:wght@400;600;700&display=swap" rel="stylesheet">
<style>
  :root {
    --bg: #e9eaec;
    --card: #ffffff;
    --name: #4b5a69;
    --title-green: #3fae2a;
    --text: #5a6270;
    --url: #6f7884;
    --icon-green: #3fae2a;
    --icon-blue: #2f7fd1;
    --icon-orange: #f39a1e;
    --icon-pink: #e2356f;
    --shadow: 0 14px 30px rgba(0,0,0,0.14), 0 2px 6px rgba(0,0,0,0.08);
  }
  * { box-sizing: border-box; margin: 0; padding: 0; }
  html, body {
    width: 1200px; height: 752px; overflow: hidden;
    background: var(--bg);
    font-family: "Open Sans", Arial, sans-serif;
  }
  .canvas {
    width: 1200px; height: 752px;
    display: flex; align-items: center; justify-content: center; gap: 40px;
  }
  .card {
    position: relative;
    width: 540px; height: 310px;
    background: var(--card);
    box-shadow: var(--shadow);
  }
  .brand-name {
    font-weight: 700;
    color: var(--name);
    line-height: 1;
  }
  /* front */
  .card-front .brand-name {
    position: absolute; left: 56px; top: 124px;
    font-size: 52px;
  }
  .contact-block {
    position: absolute; left: 262px; top: 64px;
  }
  .person-name {
    font-size: 20px; font-weight: 700; color: var(--name);
  }
  .person-title {
    font-size: 13px; font-weight: 400; color: var(--title-green);
    margin-top: 1px;
  }
  .contact-list {
    list-style: none; margin-top: 26px;
  }
  .contact-list li {
    display: flex; align-items: center; gap: 10px;
    font-size: 14px; color: var(--text);
    height: 23px;
  }
  .contact-list svg { width: 13px; height: 13px; flex: none; }
  /* back */
  .card-back {
    display: flex; flex-direction: column; align-items: center; justify-content: center;
  }
  .card-back .brand-name { font-size: 50px; }
  .card-back .site {
    margin-top: 22px;
    font-size: 14px; font-weight: 600; color: var(--url);
    letter-spacing: 0.3px;
  }
</style>
</head>
<body>
<main class="canvas">
  <section class="card card-front" aria-label="Frente do cartão">
    <span class="brand-name">vek</span>
    <div class="contact-block">
      <h1 class="person-name">Tiago Lauro Bettencourt</h1>
      <p class="person-title">CEO</p>
      <ul class="contact-list">
        <li>
          <svg viewBox="0 0 16 16" aria-hidden="true"><path fill="var(--icon-green)" d="M1 5c0-2 2-3 7-3s7 1 7 3v1.5h-3.5V5h-7v1.5H1zM3 8l2-3h6l2 3v6H3z"/><circle cx="8" cy="10.5" r="1.8" fill="#fff"/></svg>
          <span>11 96048 2195</span>
        </li>
        <li>
          <svg viewBox="0 0 16 16" aria-hidden="true"><rect x="4" y="1" width="8" height="14" rx="1.5" fill="var(--icon-blue)"/><rect x="5.5" y="3" width="5" height="7" fill="#fff"/></svg>
          <span>11 3516-9240</span>
        </li>
        <li>
          <svg viewBox="0 0 16 16" aria-hidden="true"><rect x="1" y="3" width="14" height="10" rx="1" fill="var(--icon-orange)"/><path d="M1.5 3.5 8 9l6.5-5.5" fill="none" stroke="#fff" stroke-width="1.3"/></svg>
          <span>tiago@solaria.com.br</span>
        </li>
        <li>
          <svg viewBox="0 0 16 16" aria-hidden="true"><circle cx="8" cy="8" r="7" fill="var(--icon-pink)"/><g fill="none" stroke="#fff" stroke-width="1"><ellipse cx="8" cy="8" rx="3" ry="6"/><path d="M2 8h12M3 5h10M3 11h10"/></g></svg>
          <span>www.solaria.com.br</span>
        </li>
      </ul>
    </div>
  </section>

  <section class="card card-back" aria-label="Verso do cartão">
    <span class="brand-name">vek</span>
    <p class="site">www.solaria.com.br</p>
  </section>
</main>
</body>
</html>
```